VORLEK TPMS
Website design
VORLEK TPMS - Automotive
Creative Brief
Automotive
www.VORLEKTPMS.example
TPMS is Tire Pressure Monitor Sensor. The go inside your vehicles tires and transmit information to your dashboard indicating what your tire's air pressure is. Vorlek TPMS designs, engineers and manufactures TPMS.
LIKES: Left hand navigation by vehicle (TPMS for Brisca, TPMS for QDN, TPMS for Palverine" etc etc), Year Make Model search box in content area", Modern colors, easy to navigate, professional design. DISLIKES: Busy page, hard to navigate, cluttered look.
Elegant
Modern, new colors
left side
IMPORTANT:Please see attachment for logos and layout template.

```html
<!DOCTYPE html>
<html lang="en">
<head>
<meta charset="utf-8">
<title>Vorlek TPMS</title>
<link href="https://fonts.googleapis.com/css2?family=Arimo:wght@400;700&display=swap" rel="stylesheet">
<style>
:root{
  --bg:#dcdcdc;
  --page:#ffffff;
  --blue:#1f6fb5;
  --blue-dark:#0d3f73;
  --navy:#0b2a4e;
  --grey-bar:#e9e9e9;
  --grey-line:#cfcfcf;
  --grey-panel:#f1f1f1;
  --grey-btn:#9a9a9a;
  --text:#4a4a4a;
  --muted:#888;
}
*{box-sizing:border-box;margin:0;padding:0}
html,body{width:1200px;height:1040px;overflow:hidden}
body{background:var(--bg);font-family:"Arimo",Arial,sans-serif;color:var(--text);position:relative}
.page{position:absolute;left:132px;top:0;width:936px;height:1040px;background:var(--page);box-shadow:0 0 8px rgba(0,0,0,.15)}
.abs{position:absolute}
.logo{left:20px;top:38px;font-weight:700;font-size:44px;color:var(--blue);letter-spacing:2px;line-height:1}
.logo-dot{left:20px;top:92px;width:10px;height:10px;border-radius:50%;background:var(--blue)}
.nav{left:250px;top:104px;width:672px;height:34px;background:linear-gradient(#f4f4f4,#dcdcdc);border:1px solid var(--grey-line);display:flex}
.nav a{flex:1;text-align:center;font-size:13px;line-height:32px;color:var(--muted);text-decoration:none;border-right:1px solid #fff}
.nav a.active{background:linear-gradient(#2b82cc,var(--blue-dark));color:#fff;flex:0.85}
.crumb{left:250px;top:146px;font-size:11px;color:var(--muted)}
.sidebar{left:17px;top:171px;width:216px}
.sidebar h2{background:linear-gradient(#6f6f6f,#4c4c4c);color:#fff;font-size:13px;text-align:center;height:26px;line-height:26px}
.sidebar ul{list-style:none;background:#ececec;border:1px solid var(--grey-line)}
.sidebar li{height:24.5px;line-height:24px;font-size:11.5px;color:#777;padding-left:12px;border-bottom:1px solid #fff}
.sidebar li::before{content:"» ";color:#999}
.hero{left:250px;top:169px;width:663px;height:286px;background:radial-gradient(circle at 55% 45%,#e2e2e2 0,#9a9a9a 45%,#2c2c2c 100%)}
.hero-caption{left:250px;top:415px;width:663px;height:40px;background:rgba(0,0,0,.65);color:#fff;font-size:11.5px;padding:6px 14px;line-height:14px}
.dots{right:10px;bottom:6px;display:flex;gap:4px}
.dots i{width:7px;height:7px;background:#777;display:block}
.dots i.on{background:var(--blue)}
.search{left:250px;top:478px;width:663px;height:28px;display:flex;gap:10px;align-items:center}
.select{flex:1;height:26px;border:1px solid var(--grey-line);background:#f7f7f7;font-size:11px;color:var(--muted);text-align:center;line-height:24px;position:relative;padding-right:24px}
.select::after{content:"▾";position:absolute;right:0;top:0;width:24px;height:24px;background:#777;color:#fff}
.go{width:30px;height:26px;background:var(--blue);border-radius:2px}
.welcome{left:250px;top:525px;width:663px;height:253px;background:var(--grey-panel);border:1px solid var(--grey-line);padding:14px 16px}
.welcome h3{color:var(--blue);font-size:13px;margin-bottom:8px}
.w-img{float:left;width:148px;height:104px;margin:0 12px 6px 0;background:radial-gradient(circle at 50% 40%,#eee,#8b8b8b 70%,#3a3a3a)}
.welcome p{font-size:10.5px;line-height:13px;margin-bottom:6px}
.btn{display:inline-block;background:var(--grey-btn);color:#fff;font-size:10.5px;padding:4px 10px}
.welcome .btn{position:absolute;right:12px;bottom:10px}
.col{top:795px;width:211px;height:160px;border:1px solid var(--grey-line);background:var(--grey-panel)}
.col h4{background:linear-gradient(#2b82cc,var(--blue-dark));color:#fff;font-size:12.5px;text-align:center;height:28px;line-height:28px}
.col .body{padding:10px 12px;font-size:10.5px;line-height:12.5px}
.more{color:var(--blue)}
.news p{margin-bottom:16px}
.date{float:left;width:34px;text-align:center;border:1px solid var(--grey-line);background:#fff;margin-right:8px}
.date b{display:block;font-size:16px;color:#333}
.date span{display:block;font-size:9px;color:var(--muted)}
.col .btn{position:absolute;right:12px;bottom:10px}
.quote{font-size:26px;color:#999;float:left;line-height:22px;margin-right:6px}
.footer{left:0;top:970px;width:936px;height:70px;background:linear-gradient(var(--blue-dark),var(--navy))}
.copy{left:20px;top:26px;color:#dfe8f3;font-size:10.5px}
.net{right:24px;top:10px;color:#fff;font-size:10.5px;text-align:right}
.icons{display:flex;gap:5px;margin-top:6px;justify-content:flex-end}
.icons i{width:22px;height:22px;border-radius:50%;background:#5d8fc7;display:block}
</style>
</head>
<body>
<div class="page">
  <div class="abs logo">VORLEK TPMS</div>

  <nav class="abs nav">
    <a class="active" href="#">HOME</a><a href="#">ABOUT</a><a href="#">PRODUCTS</a><a href="#">ACCESSORIES</a><a href="#">CONTACT</a>
  </nav>
  <div class="abs crumb">You are here: Home</div>

  <aside class="abs sidebar">
    <h2>OUR PRODUCTS</h2>
    <ul>
      <li>TPMS for Lorem Ipsum</li><li>TPMS for Lorem Ipsum</li><li>TPMS for Lorem Ipsum</li><li>TPMS for Lorem Ipsum</li>
      <li>TPMS for Lorem Ipsum</li><li>TPMS for Lorem Ipsum</li><li>TPMS for Lorem Ipsum</li><li>TPMS for Lorem Ipsum</li>
      <li>TPMS for Lorem Ipsum</li><li>TPMS for Lorem Ipsum</li><li>TPMS for Lorem Ipsum</li><li>TPMS for Lorem Ipsum</li>
      <li>TPMS for Lorem Ipsum</li><li>TPMS for Lorem Ipsum</li><li>TPMS for Lorem Ipsum</li><li>TPMS for Lorem Ipsum</li>
    </ul>
  </aside>

  <div class="abs hero" role="img" aria-label="Photo of a hand holding a tire pressure gauge on a car tire valve"></div>
  <div class="abs hero-caption">TPMS, goes inside your vehicles tires and transmit information to your dashboard indicating what your tire's air pressure is.
    <div class="abs dots"><i class="on"></i><i></i><i></i><i></i></div>
  </div>

  <div class="abs search">
    <div class="select">- Select Year -</div>
    <div class="select">- Select Make -</div>
    <div class="select">- Select Model -</div>
    <div class="go"></div>
  </div>

  <section class="abs welcome">
    <h3>WELCOME TO VORLEK</h3>
    <div class="w-img" role="img" aria-label="Photo of a tire pressure gauge dial"></div>
    <p>Lorem ipsum dolor sit amet, consectetur adipisicing elit, sed do eiusmod tempor incididunt ut labore et dolore magna aliqua. Ut enim ad minim veniam, quis nostrud exercitation ullamco laboris nisi ut aliquip ex ea commodo consequat. Duis aute irure dolor in reprehenderit in voluptate velit esse cillum dolore eu fugiat nulla pariatur. Excepteur sint occaecat cupidatat non proident, sunt in culpa qui officia deserunt mollit anim id est laborum.</p>
    <p style="clear:both">Lorem ipsum dolor sit amet, consectetur adipisicing elit, sed do eiusmod tempor incididunt ut labore et dolore magna aliqua. Ut enim ad minim veniam, quis nostrud exercitation ullamco laboris nisi ut aliquip ex ea commodo consequat. Duis aute irure dolor in reprehenderit in voluptate velit esse cillum dolore eu fugiat nulla pariatur. Excepteur sint occaecat cupidatat non proident, sunt in culpa qui officia deserunt mollit anim id est laborum.</p>
    <span class="btn">Learn More »</span>
  </section>

  <section class="abs col news" style="left:250px">
    <h4>LATEST NEWS</h4>
    <div class="body">
      <p>Lorem ipsum dolor sit amet, consectetur adipisicing elit. Integer porta dolor... <span class="more">More »</span></p>
      <p>Lorem ipsum dolor sit amet, consectetur adipisicing elit. Integer porta dolor... <span class="more">More »</span></p>
    </div>
  </section>

  <section class="abs col" style="left:472px">
    <h4>UPCOMING EVENTS</h4>
    <div class="body">
      <div class="date"><b>29</b><span>JUN</span></div>
      <p><b>Webinar on Lorem Ipsum</b><br>Lorem ipsum dolor sit amet, consectetur adipisicing elit. Integer porta dolor. Lorem ipsum dolor sit amet, cons.</p>
    </div>
    <span class="btn">Learn More »</span>
  </section>

  <section class="abs col" style="left:703px">
    <h4>TESTIMONIALS</h4>
    <div class="body">
      <span class="quote">“</span>
      <p>Lorem ipsum dolor sit amet, consectetur adipisicing elit. Integer porta dolor. Lorem ipsum dolor sit amet, consectetur.</p>
      <p style="margin-top:6px"><b>John Doe, ABC Co., TX</b></p>
    </div>
    <span class="btn">Learn More »</span>
  </section>

  <footer class="abs footer">
    <div class="abs copy">Copyright © 2012 VORLEKTPMS. VORLEKTPMS.example. All Rights Reserved.</div>
    <div class="abs net">networking
      <div class="icons"><i></i><i></i><i></i></div>
    </div>
  </footer>
</div>
</body>
</html>
```